Post Lockdown Ortho Special

We are running a special for (Ortho) Braces/Clear Aligner (Quorventa), till July 31st 2020. Up to $2,000 off with free Consultation and Xrays.

We need a ad to run in different formats.

Maybe something with: what better time to get braces when you have to wear a mask all the time.

Trying to rebuild our business and get people in for free consultations.

```html
<!DOCTYPE html>
<html lang="en">
<head>
<meta charset="utf-8">
<title>Post Lockdown Ortho Special</title>
<link rel="stylesheet" href="https://fonts.googleapis.com/css2?family=Montserrat:wght@400;500&family=Mulish:wght@400;500;700;800&display=swap">
<style>
  :root {
    --purple: #6a3d9a;
    --purple-deep: #5b2f8c;
    --ink: #222228;
    --ink-soft: #3a3a44;
    --sky-left: #d9e5f1;
    --sky-right: #f3f6fa;
    --white: #ffffff;
    --line-grey: #b9b4c4;
  }
  * { margin: 0; padding: 0; box-sizing: border-box; }
  html, body { width: 1200px; height: 778px; overflow: hidden; background: #6b6b6b; }
  .ad {
    position: relative;
    width: 1200px; height: 778px;
    overflow: hidden;
    background: linear-gradient(90deg, var(--sky-left) 0%, #e8eff6 40%, var(--sky-right) 70%);
    font-family: "Mulish", sans-serif;
    color: var(--ink);
  }
  .hero-photo {
    position: absolute; left: 521px; top: 0; width: 679px; height: 560px;
    background:
      radial-gradient(ellipse 40% 55% at 68% 45%, #e8c2a4 0%, rgba(232,194,164,0) 70%),
      radial-gradient(ellipse 55% 70% at 72% 50%, #b88a5e 0%, rgba(184,138,94,0) 75%),
      linear-gradient(90deg, rgba(240,244,249,0) 0%, #dfd6cc 35%, #c9b4a0 100%);
    -webkit-mask-image: linear-gradient(90deg, transparent 0%, #000 30%);
            mask-image: linear-gradient(90deg, transparent 0%, #000 30%);
  }
  .base-band { position: absolute; left: 0; top: 0; width: 1200px; height: 778px; }
  .tagline {
    position: absolute; left: 40px; width: 566px; top: 68px;
    text-align: center;
    font-family: "Montserrat", sans-serif; font-weight: 400;
    font-size: 28px; line-height: 35px; letter-spacing: 0.3px;
    color: var(--ink);
  }
  .offer-frame {
    position: absolute; left: 59px; top: 222px; width: 531px; height: 136px;
    border: 2px solid var(--purple); border-radius: 12px;
  }
  .offer-label {
    position: absolute; left: 0; width: 646px; top: 207px;
    text-align: center; font-size: 22px; font-weight: 500; color: var(--ink);
  }
  .offer-label span { background: #e6edf5; padding: 0 8px; }
  .offer-title {
    position: absolute; left: 40px; width: 566px; top: 243px;
    text-align: center; font-weight: 800; font-size: 34px; line-height: 45px;
    color: var(--purple);
  }
  .deadline {
    position: absolute; left: 181px; top: 337px; width: 282px; height: 42px;
    background: var(--purple); color: var(--white);
    font-size: 28px; font-weight: 500; line-height: 42px; text-align: center;
  }
  .deadline b { font-weight: 700; }
  .saving { position: absolute; left: 172px; top: 418px; }
  .saving .lead { font-size: 32px; line-height: 36px; color: var(--ink); }
  .saving .amount { font-size: 30px; line-height: 40px; color: var(--ink); }
  .saving .amount strong { font-size: 37px; font-weight: 800; color: var(--purple); }
  .saving-divider {
    position: absolute; left: 343px; top: 434px; width: 1px; height: 63px; background: var(--line-grey);
  }
  .saving-extra {
    position: absolute; left: 362px; top: 433px;
    font-size: 19px; line-height: 22.5px; font-weight: 500; color: var(--ink);
  }
  .gallery { position: absolute; left: 50px; top: 549px; display: flex; gap: 16px; }
  .gallery-tile {
    width: 184px; height: 94px; border-bottom-right-radius: 18px;
    box-shadow: 3px 4px 6px rgba(0,0,0,0.28);
  }
  .tile-braces { background: linear-gradient(135deg, #efe3dc, #d79a94 55%, #efeae6); }
  .tile-checkup { background: linear-gradient(90deg, #f1d2c1 0%, #e6b3a4 55%, #4e9599 100%); }
  .tile-aligner { background: linear-gradient(135deg, #2e3a3f, #5b6b4b 50%, #d9d6d4 80%, #3d4a3b); }
  .contact { position: absolute; left: 50px; font-size: 19px; color: var(--ink); display: flex; align-items: center; }
  .contact svg { flex: none; }
  .contact-address { top: 680px; }
  .contact-address svg { margin-right: 10px; }
  .contact-lines { top: 716px; }
  .contact-lines .phone-icon { margin-right: 10px; }
  .contact-lines .call { margin-right: 8px; }
  .contact-lines .phone { font-size: 28px; font-weight: 800; color: var(--purple); margin-right: 18px; }
  .contact-lines .web-icon { margin-right: 9px; }
  .practice {
    position: absolute; left: 780px; top: 600px; width: 390px; height: 140px;
    display: flex; align-items: center; gap: 18px;
  }
  .practice-dot { width: 84px; height: 84px; border-radius: 50%; background: var(--purple); flex: none; }
  .practice-name {
    font-family: "Mulish", sans-serif; font-weight: 700; color: var(--purple);
    font-size: 30px; line-height: 32px; letter-spacing: 0.5px;
  }
  .practice-name .sub { display: block; font-size: 15px; line-height: 24px; letter-spacing: 5px; }
  .practice-name .doc { display: block; font-size: 14px; line-height: 20px; letter-spacing: 1.5px; }
</style>
</head>
<body>
<main class="ad">
  <div class="hero-photo" role="img" aria-label="Smiling teenage girl in glasses holding a dental model with braces and a clear aligner"></div>

  <svg class="base-band" width="1200" height="778" viewBox="0 0 1200 778" aria-hidden="true">
    <polygon points="0,602 696,602 730,560 1200,560 1200,778 0,778" fill="#ffffff"/>
    <polygon points="696,602 710,602 746,560 732,560" fill="#6a3d9a" transform="translate(-8,-1)"/>
  </svg>

  <h1 class="tagline">KEEPING YOU IN<br>EXCELLENT ORAL HEALTH</h1>

  <div class="offer-frame"></div>
  <p class="offer-label"><span>Special for</span></p>
  <h2 class="offer-title">Ortho Braces/<br>Clear Aligner (Quorventa)</h2>
  <p class="deadline">till <b>July 31st 2020</b></p>

  <div class="saving">
    <p class="lead">Up to</p>
    <p class="amount"><strong>$2000</strong> off</p>
  </div>
  <div class="saving-divider"></div>
  <p class="saving-extra">with free<br>Consultation<br>and Xrays</p>

  <div class="gallery">
    <div class="gallery-tile tile-braces" role="img" aria-label="Close-up of a smile with metal braces"></div>
    <div class="gallery-tile tile-checkup" role="img" aria-label="Patient having a dental check-up"></div>
    <div class="gallery-tile tile-aligner" role="img" aria-label="Hand holding a clear aligner tray"></div>
  </div>

  <p class="contact contact-address">
    <svg width="24" height="24" viewBox="0 0 24 24" aria-hidden="true">
      <circle cx="12" cy="12" r="11" fill="none" stroke="#b9b4c4" stroke-width="1.2"/>
      <path d="M12 5.5a4 4 0 0 0-4 4c0 3 4 8 4 8s4-5 4-8a4 4 0 0 0-4-4z" fill="#6a3d9a"/>
      <circle cx="12" cy="9.5" r="1.5" fill="#fff"/>
    </svg>
    418 N Aspen Ridge Rd, Flagstaff, AZ 86001, United States
  </p>
  <p class="contact contact-lines">
    <svg class="phone-icon" width="24" height="24" viewBox="0 0 24 24" aria-hidden="true">
      <circle cx="12" cy="12" r="11" fill="none" stroke="#b9b4c4" stroke-width="1.2"/>
      <path d="M8.5 6.5l2 2.3-1 1.3c.8 1.7 2 2.9 3.6 3.7l1.3-1 2.3 2-1.2 1.6c-3.8-.6-7.1-3.9-7.9-7.8z" fill="#6a3d9a"/>
    </svg>
    <span class="call">Call Today</span>
    <span class="phone">928-555-0182</span>
    <svg class="web-icon" width="24" height="24" viewBox="0 0 24 24" aria-hidden="true">
      <circle cx="12" cy="12" r="11" fill="none" stroke="#b9b4c4" stroke-width="1.2"/>
      <g fill="none" stroke="#6a3d9a" stroke-width="1.2">
        <circle cx="12" cy="12" r="6.5"/>
        <ellipse cx="12" cy="12" rx="3" ry="6.5"/>
        <line x1="5.5" y1="12" x2="18.5" y2="12"/>
        <line x1="6.5" y1="9" x2="17.5" y2="9"/>
        <line x1="6.5" y1="15" x2="17.5" y2="15"/>
      </g>
    </svg>
    <span class="web">www.pinecrestsmiles.com</span>
  </p>

  <div class="practice">
    <div class="practice-dot"></div>
    <p class="practice-name">PINECREST
      <span class="sub">FAMILY DENTISTRY</span>
      <span class="doc">DR HELENA MARSH</span>
    </p>
  </div>
</main>
</body>
</html>
```